Quiet Harbor Business Card
QH biz card design 1
Quiet Harbor Business Card - Funerals
Creative Brief
Simple
Marcus Pelley
2417 Linden Crossway, Ste 42 Brookvale, MN 55190
marcus@quietharbr.com
www.quietharbr.com

```html
<!DOCTYPE html>
<html lang="en">
<head>
<meta charset="utf-8">
<title>Quiet Harbor Business Card</title>
<link href="https://fonts.googleapis.com/css2?family=Open+Sans:wght@400;600;700&display=swap" rel="stylesheet">
<style>
  :root {
    --backdrop: #e6e6e6;
    --card: #2b2c2e;
    --card-back: #1e1f21;
    --ink: #f2f2f2;
    --muted: #c9ccd2;
    --accent: #5b7fd6;
    --emboss: #141516;
    --deco: #34363a;
  }
  * { margin: 0; padding: 0; box-sizing: border-box; }
  html, body { width: 1200px; height: 802px; overflow: hidden; }
  body {
    background: var(--backdrop);
    font-family: "Open Sans", Arial, sans-serif;
    position: relative;
  }
  .card {
    position: absolute;
    top: 246px;
    width: 540px;
    height: 310px;
    box-shadow: 0 10px 24px rgba(0,0,0,.22);
    overflow: hidden;
  }
  .card-front { left: 40px; background: var(--card); }
  .card-back { left: 620px; background: var(--card-back); display: flex; align-items: center; justify-content: center; }

  .brand {
    position: absolute; left: 34px; top: 40px;
    display: flex; align-items: center; gap: 12px;
  }
  .brand-mark { width: 22px; height: 22px; background: var(--accent); }
  .brand-name {
    color: var(--ink); font-weight: 600; font-size: 25px;
    letter-spacing: 2px; text-transform: uppercase; line-height: 1;
  }

  .contact { position: absolute; left: 34px; top: 128px; }
  .person {
    color: var(--accent); font-weight: 700; font-size: 17px;
    letter-spacing: 1px; text-transform: uppercase; margin-bottom: 12px;
  }
  .contact-list { list-style: none; }
  .contact-list li {
    display: flex; align-items: center; gap: 10px;
    color: var(--muted); font-size: 13px; line-height: 22px;
  }
  .contact-list svg { width: 12px; height: 12px; flex: none; }

  .decoration {
    position: absolute; right: 30px; top: 26px; width: 190px; height: 120px;
    background: linear-gradient(135deg, var(--deco), var(--card));
  }
  .address {
    position: absolute; right: 34px; top: 170px; text-align: right;
    color: var(--muted); font-size: 13px; line-height: 20px; font-style: normal;
  }

  .edge-band { position: absolute; left: 0; bottom: 0; width: 100%; height: 8px; display: flex; }
  .edge-band .light { width: 38%; background: var(--ink); }
  .edge-band .blue { flex: 1; background: var(--accent); }

  .back-name {
    color: var(--emboss); font-weight: 600; font-size: 34px;
    letter-spacing: 3px; text-transform: uppercase;
  }
</style>
</head>
<body>
  <section class="card card-front">
    <div class="brand">
      <span class="brand-mark"></span>
      <span class="brand-name">Quiet Harbor</span>
    </div>

    <div class="decoration" role="img" aria-label="Faint decorative emblem area"></div>

    <div class="contact">
      <p class="person">Marcus Pelley</p>
      <ul class="contact-list">
        <li>
          <svg viewBox="0 0 12 12"><path d="M2.5 1h2l1 2.5-1.2.8a6 6 0 0 0 3.4 3.4l.8-1.2 2.5 1v2a1 1 0 0 1-1 1A9 9 0 0 1 1.5 2a1 1 0 0 1 1-1z" fill="var(--accent)"/></svg>
          651-555-0142
        </li>
        <li>
          <svg viewBox="0 0 12 12"><rect x="3" y="0.5" width="6" height="11" rx="1" fill="none" stroke="var(--ink)" stroke-width="1.2"/><circle cx="6" cy="9.5" r=".7" fill="var(--ink)"/></svg>
          651-555-0187
        </li>
        <li>
          <svg viewBox="0 0 12 12"><rect x="0.6" y="2.5" width="10.8" height="7" fill="none" stroke="var(--accent)" stroke-width="1.2"/><path d="M1 3l5 3.5L11 3" fill="none" stroke="var(--accent)" stroke-width="1.2"/></svg>
          marcus@quietharbr.com
        </li>
        <li>
          <svg viewBox="0 0 12 12"><circle cx="6" cy="6" r="5.2" fill="none" stroke="var(--accent)" stroke-width="1.2"/><path d="M1 6h10M6 .8c-2.5 3-2.5 7.4 0 10.4M6 .8c2.5 3 2.5 7.4 0 10.4" fill="none" stroke="var(--accent)" stroke-width="1"/></svg>
          www.quietharbr.com
        </li>
      </ul>
    </div>

    <address class="address">
      2417 Linden Crossway, Ste 42<br>
      Brookvale, MN 55190
    </address>

    <div class="edge-band"><span class="light"></span><span class="blue"></span></div>
  </section>

  <section class="card card-back">
    <p class="back-name">Quiet Harbor</p>
  </section>
</body>
</html>
```